Discreet simple classy for adult entertainment

I would like a matte black business card with gold writing for my business. Keeping it simple. Having my following:

Lana frost
Events. Entertainment. Promotions
0491726580

or alternatively could have what i had on my previous card below but i think i prefer the above as again - discretion.

Maybe a nice gold line thru the card or some other very simple design . Or not open to ideas/ can be doublesided if any good ideas with that.

included pics of my old bus card. not sure weather i want a photo on it or not. if i do it wont be the same pic. i kinda wanted a card that was discreet so if it was in someones wallet they wouldn't neccessarily realise it was from a stripper.

Target Market(s)

men

Industry/Entity Type

Business

Contact Information for Business Card

Lana frost
0491726580

Requirements
Nice to have
• i don't know i am really open to anything. im giving my cards to guys so something they can have in their wallet that is discreet preferably.

```html
<!DOCTYPE html>
<html lang="en">
<head>
<meta charset="utf-8">
<title>Lana frost — Business Card</title>
<link href="https://fonts.googleapis.com/css2?family=Arimo:ital,wght@0,400;1,700&family=Kaushan+Script&display=swap" rel="stylesheet">
<style>
  :root {
    --gold: #f2d23a;
    --gold-deep: #c9a82a;
    --band-light: #e9c84a;
    --band-dark: #c9a630;
    --card-black: #0d0d0d;
    --card-black-edge: #050505;
    --silver-top: #ffffff;
    --silver-bottom: #b9b9b9;
  }
  * { margin: 0; padding: 0; box-sizing: border-box; }
  html, body {
    width: 741px;
    height: 1200px;
    overflow: hidden;
    background: var(--card-black-edge);
  }
  .card {
    position: relative;
    width: 741px;
    height: 1200px;
    overflow: hidden;
    background: radial-gradient(ellipse at 50% 45%, #1a1a1a 0%, var(--card-black) 55%, var(--card-black-edge) 100%);
  }
  .band {
    position: absolute;
    left: 0;
    width: 100%;
    background: linear-gradient(180deg, var(--band-light), var(--band-dark));
  }
  .band--top { top: 0; height: 100px; }
  .band--bottom { bottom: 0; height: 38px; }

  .name {
    position: absolute;
    top: 150px;
    left: 0;
    width: 100%;
    text-align: center;
    font-family: "Kaushan Script", cursive;
    font-size: 118px;
    line-height: 1.2;
    color: var(--gold);
    text-shadow: 0 2px 0 var(--gold-deep);
  }
  .flourish {
    position: absolute;
    top: 320px;
    left: 50px;
    width: 641px;
    height: 100px;
  }

  .phone-icon {
    position: absolute;
    top: 557px;
    left: 310px;
    width: 120px;
    height: 120px;
  }
  .phone-number {
    position: absolute;
    top: 722px;
    left: 0;
    width: 100%;
    text-align: center;
    font-family: "Arimo", sans-serif;
    font-style: italic;
    font-weight: 700;
    font-size: 92px;
    letter-spacing: 1px;
    color: var(--silver-top);
    background: linear-gradient(180deg, var(--silver-top) 45%, var(--silver-bottom));
    -webkit-background-clip: text;
    background-clip: text;
    -webkit-text-fill-color: transparent;
  }

  .services {
    position: absolute;
    top: 955px;
    left: 62px;
    width: 640px;
    list-style: none;
    display: flex;
    flex-wrap: wrap;
    row-gap: 14px;
    font-family: "Arimo", sans-serif;
    font-size: 48px;
    color: var(--gold);
  }
  .services__item {
    display: flex;
    align-items: center;
    margin-right: 24px;
    line-height: 52px;
  }
  .services__item--break { flex-basis: 100%; }
  .tick {
    width: 24px;
    height: 24px;
    margin-right: 14px;
    margin-top: 8px;
  }
</style>
</head>
<body>
  <main class="card">
    <div class="band band--top"></div>

    <h1 class="name">Lana frost</h1>

    <svg class="flourish" role="img" aria-label="Gold ornamental flourish divider" viewBox="0 0 641 100">
      <defs>
        <radialGradient id="flourishGlow" cx="50%" cy="40%" r="50%">
          <stop offset="0%" stop-color="#f2d23a" stop-opacity="0.35"/>
          <stop offset="100%" stop-color="#f2d23a" stop-opacity="0"/>
        </radialGradient>
      </defs>
      <rect x="0" y="0" width="641" height="100" fill="url(#flourishGlow)"/>
    </svg>

    <svg class="phone-icon" viewBox="0 0 120 120" aria-hidden="true">
      <circle cx="60" cy="60" r="54" fill="none" stroke="#f2d23a" stroke-width="5"/>
      <path d="M48 34c4-3 8-2 10 2l5 10c1 3 0 5-2 7l-4 3c2 8 6 14 12 19l4-3c2-2 5-2 7 0l8 8c3 3 2 7-1 9l-5 4c-4 3-10 2-15-2-14-11-22-25-24-42 0-6 2-11 5-14z" fill="#f2d23a"/>
    </svg>

    <p class="phone-number">0491726580</p>

    <ul class="services">
      <li class="services__item">
        <svg class="tick" viewBox="0 0 24 24" aria-hidden="true"><path d="M3 12l6 6L21 5" fill="none" stroke="#f2d23a" stroke-width="4" stroke-linecap="round" stroke-linejoin="round"/></svg>
        Events
      </li>
      <li class="services__item">
        <svg class="tick" viewBox="0 0 24 24" aria-hidden="true"><path d="M3 12l6 6L21 5" fill="none" stroke="#f2d23a" stroke-width="4" stroke-linecap="round" stroke-linejoin="round"/></svg>
        Entertainment.
      </li>
      <li class="services__item services__item--break">
        <svg class="tick" viewBox="0 0 24 24" aria-hidden="true"><path d="M3 12l6 6L21 5" fill="none" stroke="#f2d23a" stroke-width="4" stroke-linecap="round" stroke-linejoin="round"/></svg>
        Promotions
      </li>
    </ul>

    <div class="band band--bottom"></div>
  </main>
</body>
</html>
```